Front & Back Book Cover Design

Title:
THE QUIET LANDLORD: How to Grow Comfort and Plenty Through Property Held by Others
Author:
Mel T. Varnak
Design Philosophy:
A modern, minimalist-luxury aesthetic that feels visionary and intelligent — positioned between business innovation (The Brisk Venture), modern finance (The Anatomy of Thrift), and timeless real estate insight (Bold Aunt Meek Aunt).
Think: clean, bold, and idea-driven — a visual reflection of the book’s central concept: wealth through clarity, not clutter.
Back Cover:
To include book description along with author photo and bio
Files:
PNG, PDF, EPUB

```html
<!DOCTYPE html>
<html lang="en">
<head>
<meta charset="utf-8">
<title>The Quiet Landlord — Cover Spread</title>
<link href="https://fonts.googleapis.com/css2?family=Oswald:wght@500;700&family=Roboto+Condensed:wght@400;700&family=Roboto:wght@300&display=swap" rel="stylesheet">
<style>
  :root {
    --stage: #6b6b6b;
    --paper: #ffffff;
    --paper-fade: #c3c7cc;
    --ink: #3a3b3d;
    --ink-soft: #8a8c8f;
    --red: #c3253a;
    --shadow-type: #c9cbce;
    --gold: #c39a45;
    --gold-light: #e6d6ad;
    --glass: #eceef0;
  }
  html, body {
    margin: 0;
    width: 1200px;
    height: 2182px;
    overflow: hidden;
    background: var(--stage);
  }
  .spread {
    position: absolute;
    left: 57px;
    top: 707px;
    width: 1086px;
    height: 768px;
    background: linear-gradient(180deg, var(--paper) 0%, var(--paper) 80%, var(--paper-fade) 100%);
    box-shadow: 0 10px 24px rgba(0,0,0,.35);
    overflow: hidden;
  }
  .type-layer {
    position: absolute;
    inset: 0;
    width: 1086px;
    height: 768px;
  }
  .title-line { font-family: "Oswald", sans-serif; font-weight: 700; }
  .title-line.dark { fill: var(--ink); }
  .title-line.red { fill: var(--red); }
  .title-line.ghost { fill: var(--shadow-type); }
  .subtitle { font-family: "Roboto", sans-serif; font-weight: 300; font-size: 21px; fill: #2c2c2e; }
  .spine-title { font-family: "Oswald", sans-serif; font-weight: 700; font-size: 27px; letter-spacing: 3px; }
  .spine-author { font-family: "Roboto", sans-serif; font-weight: 300; font-size: 27px; fill: #2c2c2e; }
  .back-title { font-family: "Oswald", sans-serif; font-weight: 700; font-size: 25px; }
  .front-author { font-family: "Roboto", sans-serif; font-weight: 300; font-size: 32px; fill: #222; }

  .hourglass-art {
    position: absolute;
    left: 743px;
    top: 356px;
    width: 170px;
    height: 394px;
    border-radius: 42% 42% 40% 40% / 16% 16% 12% 12%;
    background: linear-gradient(180deg, var(--glass) 0%, var(--gold-light) 18%, var(--gold) 42%, var(--glass) 52%, var(--gold-light) 75%, var(--gold) 95%);
  }

  .back-copy {
    position: absolute;
    left: 138px;
    top: 52px;
    width: 283px;
    font-family: "Roboto Condensed", sans-serif;
    font-size: 11.4px;
    line-height: 15px;
    color: #222;
    text-align: justify;
  }
  .back-copy p { margin: 0; }
  .back-copy .gap { margin-top: 10px; }
  .hook {
    color: var(--red);
    font-weight: 700;
    font-size: 13.5px;
    line-height: 17px;
    margin-bottom: 2px !important;
  }
  .point { margin-top: 3px !important; }
  .point b, .accent { color: var(--ink-soft); font-weight: 700; }
  .author-photo {
    float: left;
    width: 144px;
    height: 144px;
    margin: 24px 10px 0 -98px;
    border-radius: 50%;
    shape-outside: circle(50%);
    background: radial-gradient(circle at 50% 40%, #b89a86 0%, #6d5a50 45%, #2a2626 100%);
  }
  .closing { font-weight: 700; }
  .author-name {
    font-family: "Roboto", sans-serif;
    font-weight: 300;
    font-size: 19px;
    line-height: 22px;
    margin-top: 10px !important;
    text-align: left;
  }
  .bio-rule {
    clear: both;
    margin-top: 12px;
    width: 250px;
    border-top: 1px solid #777;
  }
</style>
</head>
<body>
  <main class="spread">
    <section class="back-copy">
      <p class="hook">What if the smartest real estate investors in the world don’t actually own anything?</p>
      <p>In a world where leverage has replaced labor and access has replaced assets, The Quiet Landlord reveals how a new generation of entrepreneurs is building wealth without deeds, mortgages, or massive capital.</p>
      <p>Mel T. Varnak exposes the hidden playbook behind modern real estate wealth — not through ownership, but through control, creativity, and influence.</p>
      <p>You’ll discover how to:</p>
      <p class="gap point">•<b>Profit from properties you never buy</b> through partnerships, performance models, and control agreements.</p>
      <p class="point">•<b>Monetize your skills, systems, and relationships</b> just like institutional investors do.</p>
      <p class="point">•<b>Build digital real estate</b> — brands, websites, and lead funnels that pay like rentals.</p>
      <p class="point">•<b>Create recurring income</b> through master leases, management contracts, and service-based equity.</p>
      <p class="point">•<b>Design your freedom formula</b>—where wealth is measured in time, not titles.</p>
      <div class="author-photo" role="img" aria-label="Round portrait photo of the author"></div>
      <p class="gap">Packed with frameworks, examples, and the mindset of modern deal-makers, The Quiet Landlord is a blueprint for the future of wealth creation — one built on access, not assets.</p>
      <p class="closing" style="font-weight:400">Because in the new economy, <span class="accent">the most powerful investors don’t own real estate. They own opportunity.</span></p>
      <p class="closing" style="color:#555">And now, you can too.</p>
      <p class="author-name">MEL T. VARNAK</p>
      <p style="margin-top:4px">Mel T. Varnak is a real estate entrepreneur and owner of Harrowgate Studio in Silver Mesa, NV and Crestline Property Partners in Harbor Point, California. Combining design, development, and deal strategy, he’s helped agents, investors, and entrepreneurs build freedom through systems — not stuff. The Quiet Landlord is his definitive guide to building wealth through creative control.</p>
      <div class="bio-rule"></div>
    </section>

    <div class="hourglass-art" role="img" aria-label="Glass hourglass with a golden city skyline in the top bulb and gold coins falling into the bottom"></div>

    <svg class="type-layer" viewBox="0 0 1086 768" aria-hidden="false">
      <!-- back cover vertical title -->
      <text class="back-title" transform="translate(118 394) rotate(-90)">
        <tspan fill="var(--ink)">THE QUIET </tspan><tspan fill="var(--red)">LANDLORD</tspan>
      </text>

      <!-- spine -->
      <text class="spine-title" transform="translate(532 55) rotate(90)">
        <tspan fill="var(--ink)">THE QUIET </tspan><tspan fill="var(--red)">LANDLORD</tspan>
      </text>
      <text class="spine-author" transform="translate(532 606) rotate(90)">Mel T. Varnak</text>

      <!-- front title -->
      <g class="front-title">
        <text class="title-line ghost" x="616" y="143" font-size="132" textLength="162" lengthAdjust="spacingAndGlyphs">THE</text>
        <text class="title-line dark" x="612" y="140" font-size="132" textLength="162" lengthAdjust="spacingAndGlyphs">THE</text>
        <text class="title-line ghost" x="616" y="262" font-size="136" textLength="436" lengthAdjust="spacingAndGlyphs">QUIET</text>
        <text class="title-line dark" x="612" y="259" font-size="136" textLength="436" lengthAdjust="spacingAndGlyphs">QUIET</text>
        <text class="title-line ghost" x="616" y="371" font-size="126" textLength="441" lengthAdjust="spacingAndGlyphs">LANDLORD</text>
        <text class="title-line red" x="612" y="368" font-size="126" textLength="441" lengthAdjust="spacingAndGlyphs">LANDLORD</text>
      </g>
      <line x1="785" y1="42" x2="785" y2="118" stroke="var(--red)" stroke-width="1.5"/>
      <text class="subtitle" x="797" y="64">How to Grow Comfort and</text>
      <text class="subtitle" x="797" y="87">Plenty Through Property</text>
      <text class="subtitle" x="797" y="110">Held by Others</text>

      <text class="front-author" x="877" y="560">Mel T. Varnak</text>
    </svg>
  </main>
</body>
</html>
```